Business Card Design Project - bel soravin group

dear Sirs

we need business card design for our group ( BEL Soravin Group ) , i have got the Logo design of our group from pixel harbor in previous , so all need details relating to our group i think available with you, as well as the the chosen logo design

we hope to provide us with business card logo that to be appropaite and satisfactory to us .

thanks

note : logo design of our group is attached .
Updates

Reason: please extend the deadline of my project for additional 15 days because i didn't received appropriate design for our gruop yet . kindly beaware that i have received 77 design till now , supossed to send me 200-250 design at least . thanks

Target Market(s)

contents
-

name : Korvan EL Mistrani

position : Operation Manager

Industry/Entity Type

Business

Requirements
Must have

• person name

group logo
Nice to have
• logo color matching with back background

```html
<!DOCTYPE html>
<html lang="en">
<head>
<meta charset="utf-8">
<title>BEL Soravin Group – Business Card</title>
<link href="https://fonts.googleapis.com/css2?family=Open+Sans:wght@400;600;700&display=swap" rel="stylesheet">
<style>
  :root {
    --backdrop: #b4892d;
    --card: #ffffff;
    --brand-blue: #17508f;
    --name-blue: #1b73b9;
    --icon-blue: #1f6db5;
    --band-top: #1976c6;
    --band-bottom: #0d4f96;
    --gold: #c9a04a;
    --gold-light: #e8cf8a;
    --title-gold: #c39a3b;
    --ink: #1d1d1d;
    --divider: #555555;
  }
  * { margin: 0; padding: 0; box-sizing: border-box; }
  html, body {
    width: 1200px; height: 686px; overflow: hidden;
    background: var(--backdrop);
    font-family: "Open Sans", Arial, sans-serif;
  }
  .canvas { position: relative; width: 1200px; height: 686px; }
  .card {
    position: absolute; width: 491px; height: 280px;
    background: var(--card); border-radius: 22px; overflow: hidden;
    box-shadow: 2px 3px 6px rgba(0,0,0,0.35);
  }
  .card--front { left: 81px; top: 108px; }
  .card--back { left: 621px; top: 310px; }
  .card__wave { position: absolute; left: 0; top: 0; width: 491px; height: 280px; }
  .card__website {
    position: absolute; left: 35px; bottom: 16px;
    color: #fff; font-weight: 700; font-size: 11.5px; letter-spacing: 1.6px;
  }
  .brand {
    position: absolute; left: 0; right: 0;
    display: flex; align-items: center; justify-content: center; gap: 10px;
    color: var(--brand-blue); font-weight: 600;
  }
  .brand__mark { background: var(--brand-blue); flex: none; }
  .brand__text { display: flex; flex-direction: column; line-height: 1; }
  .card--front .brand { top: 46px; }
  .card--front .brand__mark { width: 16px; height: 16px; }
  .card--front .brand__name { font-size: 33px; letter-spacing: 0.5px; }
  .card--front .brand__tag { font-size: 13.5px; margin-top: 4px; letter-spacing: 0.4px; }
  .card--back .brand { top: 92px; }
  .card--back .brand__mark { width: 20px; height: 20px; }
  .card--back .brand__name { font-size: 42px; letter-spacing: 0.6px; }
  .card--back .brand__tag { font-size: 17px; margin-top: 5px; letter-spacing: 0.5px; }
  .person {
    position: absolute; right: 264px; top: 132px; text-align: right; width: 200px;
  }
  .person__name { color: var(--name-blue); font-weight: 700; font-size: 15px; line-height: 19px; }
  .person__title { color: var(--title-gold); font-weight: 700; font-size: 12.5px; line-height: 19px; }
  .person__address { color: var(--ink); font-size: 12.5px; line-height: 16px; margin-top: 2px; }
  .divider {
    position: absolute; left: 241px; top: 135px; width: 1px; height: 60px; background: var(--divider);
  }
  .contacts { position: absolute; left: 256px; top: 131px; list-style: none; }
  .contacts li {
    display: flex; align-items: center; gap: 3px;
    color: var(--ink); font-size: 12.5px; height: 19.5px;
  }
  .contacts svg { width: 11px; height: 11px; fill: var(--icon-blue); flex: none; }
</style>
</head>
<body>
<div class="canvas">

  <section class="card card--front">
    <svg class="card__wave" viewBox="0 0 491 280" aria-hidden="true">
      <defs>
        <linearGradient id="band" x1="0" y1="0" x2="0" y2="1">
          <stop offset="0" stop-color="var(--band-top)"/>
          <stop offset="1" stop-color="var(--band-bottom)"/>
        </linearGradient>
        <linearGradient id="goldline" x1="0" y1="0" x2="1" y2="0">
          <stop offset="0" stop-color="var(--gold)"/>
          <stop offset="0.45" stop-color="var(--gold-light)"/>
          <stop offset="1" stop-color="var(--gold)"/>
        </linearGradient>
      </defs>
      <path d="M0,231 C120,219 250,258 345,262 C420,265 470,252 491,241 L491,247 C470,259 420,272 345,270 C250,266 120,232 0,237 Z" fill="url(#goldline)"/>
      <path d="M0,240 C120,236 250,268 345,273 C420,276 470,262 491,251 L491,280 L0,280 Z" fill="url(#band)"/>
    </svg>
    <div class="brand">
      <span class="brand__mark"></span>
      <div class="brand__text">
        <span class="brand__name">BEL SORAVIN</span>
        <span class="brand__tag">GROUP OF COMPANIES</span>
      </div>
    </div>
    <div class="person">
      <p class="person__name">Korvan EL Mistrani</p>
      <p class="person__title">Operation Manager</p>
      <p class="person__address">Street name City<br>State, zip code</p>
    </div>
    <div class="divider"></div>
    <ul class="contacts">
      <li><svg viewBox="0 0 24 24"><path d="M6.6 10.8a15 15 0 0 0 6.6 6.6l2.2-2.2c.3-.3.7-.4 1-.2 1.1.4 2.3.6 3.6.6.6 0 1 .4 1 1V20c0 .6-.4 1-1 1A17 17 0 0 1 3 4c0-.6.4-1 1-1h3.5c.6 0 1 .4 1 1 0 1.3.2 2.5.6 3.6.1.3 0 .7-.2 1z"/></svg>(TF)123-456-7890</li>
      <li><svg viewBox="0 0 24 24"><path d="M6.6 10.8a15 15 0 0 0 6.6 6.6l2.2-2.2c.3-.3.7-.4 1-.2 1.1.4 2.3.6 3.6.6.6 0 1 .4 1 1V20c0 .6-.4 1-1 1A17 17 0 0 1 3 4c0-.6.4-1 1-1h3.5c.6 0 1 .4 1 1 0 1.3.2 2.5.6 3.6.1.3 0 .7-.2 1z"/></svg>123-456-7890</li>
      <li><svg viewBox="0 0 24 24"><path d="M6 2h10v5H6zM3 8h18v10h-3v4H6v-4H3zM8 15v5h8v-5zM17 10v2h2v-2z"/></svg>123-456-7890</li>
      <li><svg viewBox="0 0 24 24"><path d="M2 5h20v14H2zM3.5 6.5l8.5 6 8.5-6z" fill-rule="evenodd"/></svg>name@belsoravin.com</li>
    </ul>
    <p class="card__website">www.belsoravin.com</p>
  </section>

  <section class="card card--back">
    <svg class="card__wave" viewBox="0 0 491 280" aria-hidden="true">
      <path d="M0,231 C120,219 250,258 345,262 C420,265 470,252 491,241 L491,247 C470,259 420,272 345,270 C250,266 120,232 0,237 Z" fill="url(#goldline)"/>
      <path d="M0,240 C120,236 250,268 345,273 C420,276 470,262 491,251 L491,280 L0,280 Z" fill="url(#band)"/>
    </svg>
    <div class="brand">
      <span class="brand__mark"></span>
      <div class="brand__text">
        <span class="brand__name">BEL SORAVIN</span>
        <span class="brand__tag">GROUP OF COMPANIES</span>
      </div>
    </div>
    <p class="card__website">www.belsoravin.com</p>
  </section>

</div>
</body>
</html>
```